Epoxy Flooring Contractor business card

We need a business card to promote a new addition to our business. We now offer Epoxy Flooring. We would like for the business card to include the images attached. One is our logo, the other is a sample of metallic epoxy flooring, we would like to incorporate that somewhere into the design. I was thinking an icon of a man pushing a concrete grinder and have the color set to the metallic epoxy color. I found a business card sample on this website, I will attach it. It has the icon that we are looking for, or something similar.
Our company name is Brightmore Coatings LLC
Our owners name is Dana Pellow
Phone is 738-847-2916
website is www.brightmore-coatingsllc.com
please let me know if you need any other info

Contact Information for Business Card

Brightmore Coatings LLC
Dana Pellow, owner
Phone: 738-847-2916
Address: P.O Box 8146 Cedar Hollow, GA 31547
www.Brightmore-CoatingsLLC.com
BrightmoreCoatingsLLC@mailvista.net
Include logo attached
It must include a Clip art of man with concrete grinder
Must include metallic epoxy design attached
Must include the following text
Residential Garage Flooring
Epoxy Countertops
Commercial Epoxy Flooring
Restaurant Flooring
Warehouse Flooring
Licensed & Insured
Free Estimates

Colors

Designer to choose colors to be used in the design.

Requirements
Must have
• Include logo attached
• It must include a Clip art of man with concrete grinder
• Must include metallic epoxy design attached
• Must include the following text
• Garage Epoxy Flooring
• Residential Epoxy Flooring
• Concrete Floor Crack Repairs
• Concrete Floor Grinding
• Commercial & Warehouse Epoxy Flooring
• Restaurant Epoxy Flooring
• Epoxy Countertops
• Non Slip Epoxy Pool Decks
• Textured Finishes, Flakes, Granite Coat, Metallic & Quartz
• FREE ESTIMATES • LICENSED & INSURED

```html
<!DOCTYPE html>
<html lang="en">
<head>
<meta charset="utf-8">
<title>Brightmore Coatings – Business Card</title>
<link rel="stylesheet" href="https://fonts.googleapis.com/css2?family=Montserrat:wght@500&family=Open+Sans:wght@400;600&family=Roboto:wght@700&display=swap">
<style>
  :root {
    --page-bg: #d9d9d9;
    --card-white: #ffffff;
    --steel: #3e5f84;
    --sky: #7aa4cf;
    --grey-text: #4a4a4a;
    --rule: #cfcfcf;
    --back-top: #79a6d0;
    --back-bottom: #41678f;
  }
  * { margin: 0; padding: 0; box-sizing: border-box; }
  html, body { width: 1200px; height: 802px; overflow: hidden; }
  body {
    background: var(--page-bg);
    position: relative;
    font-family: "Open Sans", sans-serif;
  }
  .card {
    position: absolute;
    top: 274px;
    width: 443px;
    height: 265px;
    overflow: hidden;
  }
  .card--front { left: 136px; background: var(--card-white); }
  .card--back {
    left: 624px;
    background: linear-gradient(35deg, var(--back-bottom) 0%, #5482b0 55%, var(--back-top) 100%);
    color: #fff;
    text-align: center;
  }

  /* front */
  .brand-mark {
    position: absolute;
    right: 30px;
    top: 64px;
    display: flex;
    align-items: center;
    gap: 9px;
  }
  .brand-mark__square { width: 30px; height: 30px; background: var(--sky); }
  .brand-mark__name {
    font-family: "Montserrat", sans-serif;
    font-weight: 500;
    font-size: 17px;
    line-height: 18px;
    letter-spacing: 1.2px;
    color: var(--grey-text);
  }
  .holder { position: absolute; left: 24px; top: 144px; }
  .holder__name {
    font-family: "Roboto", sans-serif;
    font-weight: 700;
    font-size: 20px;
    color: var(--steel);
    line-height: 22px;
  }
  .holder__role { font-size: 11px; color: var(--grey-text); line-height: 12px; }
  .holder-rule {
    position: absolute;
    left: 64px; right: 31px; top: 173px;
    height: 1px; background: var(--rule);
  }
  .contact {
    position: absolute;
    left: 24px; top: 199px;
    list-style: none;
    font-size: 11.5px;
    line-height: 16px;
    color: var(--grey-text);
  }
  .contact li { display: flex; align-items: center; gap: 4px; }
  .contact svg { width: 11px; height: 11px; fill: var(--steel); }
  .address {
    position: absolute;
    right: 28px; top: 199px;
    text-align: right;
    font-size: 11.5px;
    line-height: 16px;
    color: var(--grey-text);
    font-style: normal;
  }
  .address__company { font-weight: 600; color: var(--steel); }
  .accent-bar { position: absolute; left: 0; right: 0; bottom: 0; height: 7px; display: flex; }
  .accent-bar__light { width: 226px; background: var(--sky); }
  .accent-bar__dark { flex: 1; background: var(--steel); }

  /* back */
  .back-title {
    position: absolute;
    left: 0; right: 0; top: 92px;
    font-family: "Montserrat", sans-serif;
    font-weight: 500;
    font-size: 35px;
    line-height: 36px;
    letter-spacing: 2.5px;
  }
  .services {
    position: absolute;
    left: 0; right: 0; top: 198px;
    font-size: 11.4px;
    line-height: 15.6px;
    list-style: none;
  }
</style>
</head>
<body>
  <section class="card card--front" aria-label="Business card front">
    <div class="brand-mark">
      <span class="brand-mark__square"></span>
      <span class="brand-mark__name">Brightmore<br>Coatings</span>
    </div>

    <div class="holder">
      <p class="holder__name">Dana Pellow</p>
      <p class="holder__role">Owner</p>
    </div>
    <div class="holder-rule"></div>

    <ul class="contact">
      <li>
        <svg viewBox="0 0 12 12" aria-hidden="true"><path d="M1 4c0-2 2-3 5-3s5 1 5 3v1H8.5V4h-5v1H1zM3 6h6l2 5H1z"/></svg>
        738-847-2916
      </li>
      <li>
        <svg viewBox="0 0 12 12" aria-hidden="true"><path d="M0 2h12v8H0zM1 3v.4l5 3.4 5-3.4V3zm0 1.6V9h10V4.6L6 8z"/></svg>
        BrightmoreCoatingsLLC@mailvista.net
      </li>
      <li>
        <svg viewBox="0 0 12 12" aria-hidden="true"><circle cx="6" cy="6" r="5.5"/></svg>
        www.Brightmore-CoatingsLLC.com
      </li>
    </ul>

    <address class="address">
      <span class="address__company">Brightmore Coatings LLC</span><br>
      P.O Box 8146 Cedar<br>
      Hollow, GA 31547
    </address>

    <div class="accent-bar">
      <span class="accent-bar__light"></span>
      <span class="accent-bar__dark"></span>
    </div>
  </section>

  <section class="card card--back" aria-label="Business card back">
    <h1 class="back-title">Brightmore<br>Coatings</h1>
    <ul class="services">
      <li>Residential Garage Flooring ● Epoxy Countertops</li>
      <li>Commercial Epoxy Flooring ● Restaurant Flooring</li>
      <li>Warehouse Flooring ● Licensed &amp; Insured ● Free Estimates</li>
    </ul>
  </section>
</body>
</html>
```